ultra-minimalist business card

front (black background, matte):

tarik b. hosseny
writer | photographer
get@tarikhosseny.com

back (white background, matte):

a picture speaks a thousand words;
a word draws a thousand pictures.

www.tarikhosseny.com

all text should be small (white or silver - as long as it shows against the black - on the front; black or gray - as long as it shows against the white - on the back).

feel free to get creative in terms of arrangement, alignment, and font type, but remember, the overall style is minimalist, so nothing too fancy, please.

thanks.

```html
<!DOCTYPE html>
<html lang="en">
<head>
<meta charset="UTF-8">
<title>tarik b. hosseny — business card front</title>
<link rel="stylesheet" href="https://fonts.googleapis.com/css2?family=Inter:wght@300;400&display=swap">
<style>
  :root {
    --paper: #ffffff;
    --card: #1c1c1c;
    --rule: #000000;
    --ink: #ffffff;
  }
  * { margin: 0; padding: 0; box-sizing: border-box; }
  html, body {
    width: 1200px;
    height: 805px;
    overflow: hidden;
    background: var(--paper);
  }
  .canvas {
    position: relative;
    width: 1200px;
    height: 805px;
  }
  .card {
    position: absolute;
    left: 40px;
    top: 40px;
    width: 1116px;
    height: 727px;
    background: var(--card);
    overflow: hidden;
  }
  .card-rules {
    position: absolute;
    inset: 0;
    width: 100%;
    height: 100%;
  }
  .card-rules line {
    stroke: var(--rule);
    stroke-width: 4;
  }
  .name {
    position: absolute;
    left: 0;
    right: 0;
    top: 328px;
    text-align: center;
    font-family: "Inter", sans-serif;
    font-weight: 300;
    font-size: 50px;
    letter-spacing: 0.13em;
    line-height: 1;
    color: var(--ink);
  }
  .details {
    position: absolute;
    left: 0;
    right: 0;
    top: 592px;
    text-align: center;
    font-family: "Inter", sans-serif;
    font-weight: 300;
    font-size: 23px;
    line-height: 33px;
    letter-spacing: -0.01em;
    color: var(--ink);
  }
</style>
</head>
<body>
  <div class="canvas">
    <section class="card">
      <svg class="card-rules" viewBox="0 0 1116 727" aria-hidden="true">
        <line x1="0" y1="646" x2="1116" y2="372"/>
        <line x1="843" y1="727" x2="1116" y2="499"/>
      </svg>
      <h1 class="name">tarik b. hosseny</h1>
      <div class="details">
        <p class="role">writer | photographer</p>
        <p class="email">get@tarikhosseny.com</p>
      </div>
    </section>
  </div>
</body>
</html>
```